Velmar Industrial Coatings

We are looking to improve our business cards. Our company installs industrial floor and wall coatings in industrial, chemical and food processing plants.
Our coatings which consist of epoxy, urethane, and vinyl esters provide chemical and abrasion resistant surface with non-skid properties that are easy to clean.

Target Market(s)

food manufacturing, chemical plants, breweries and wineries, warehouses, clean room floors.

Industry/Entity Type

Construction

Contact Information for Business Card

improved current logo.

Colors

Designer to choose colors to be used in the design.

Requirements
Must have
• the information from uploaded file
Nice to have
• "We'll be outstanding on your floors."

```html
<!DOCTYPE html>
<html lang="en">
<head>
<meta charset="utf-8">
<title>Velmar Industrial Coatings – Business Card</title>
<link href="https://fonts.googleapis.com/css2?family=Oswald:wght@400&family=Arimo:ital,wght@0,400;1,400&display=swap" rel="stylesheet">
<style>
  :root {
    --stage: #c4c2c4;
    --green: #3a5028;
    --green-light: #45602f;
    --green-dark: #2c3d1f;
    --paper: #f7f7f6;
    --ink: #1f1f1f;
    --white: #ffffff;
  }
  html, body {
    margin: 0;
    padding: 0;
    width: 1200px;
    height: 1200px;
    overflow: hidden;
    background: var(--stage);
  }
  .stage {
    position: relative;
    width: 1200px;
    height: 1200px;
  }
  .card {
    position: absolute;
    left: 250px;
    width: 700px;
    height: 400px;
    box-shadow: 0 14px 22px rgba(0,0,0,0.35);
    overflow: hidden;
  }
  .card-front { top: 150px; background: var(--green); }
  .card-back { top: 650px; background: var(--paper); }

  .front-texture {
    position: absolute;
    inset: 0;
    background: radial-gradient(ellipse at center, var(--green-light) 0%, var(--green) 70%);
  }
  .front-title {
    position: absolute;
    left: 0; right: 0;
    top: 168px;
    text-align: center;
    font-family: 'Oswald', sans-serif;
    font-weight: 400;
    font-size: 44px;
    letter-spacing: -0.5px;
    color: var(--white);
    margin: 0;
    transform: scaleX(0.86);
  }
  .front-web {
    position: absolute;
    left: 0; right: 0;
    top: 340px;
    text-align: center;
    font-family: 'Arimo', sans-serif;
    font-style: italic;
    font-size: 27px;
    color: var(--white);
  }

  .brand {
    position: absolute;
    left: 34px;
    top: 58px;
    display: flex;
    align-items: center;
    gap: 14px;
  }
  .brand-square {
    width: 40px;
    height: 40px;
    background: var(--green-dark);
  }
  .brand-name {
    font-family: 'Oswald', sans-serif;
    font-weight: 400;
    font-size: 30px;
    color: var(--green-dark);
    letter-spacing: -0.5px;
  }
  .person {
    position: absolute;
    right: 36px;
    top: 138px;
    text-align: right;
    font-family: 'Arimo', sans-serif;
    color: var(--green-dark);
  }
  .person-name { font-size: 33px; line-height: 36px; }
  .person-tollfree { font-size: 21px; line-height: 24px; color: var(--ink); }

  .address {
    position: absolute;
    left: 34px;
    top: 262px;
    font-family: 'Arimo', sans-serif;
    font-size: 22px;
    line-height: 33px;
    color: var(--ink);
    font-style: normal;
  }
  .contacts {
    position: absolute;
    right: 34px;
    top: 248px;
    margin: 0;
    padding: 0;
    list-style: none;
    font-family: 'Arimo', sans-serif;
    font-size: 20px;
    line-height: 28.5px;
    color: var(--ink);
    text-align: right;
  }
  .contacts li {
    display: flex;
    justify-content: flex-end;
    align-items: center;
    gap: 12px;
  }
  .contacts svg {
    width: 18px;
    height: 18px;
    fill: var(--green-dark);
    flex: none;
  }
</style>
</head>
<body>
<main class="stage">
  <section class="card card-front">
    <div class="front-texture" role="img" aria-label="Subtle green grid pattern background"></div>
    <h1 class="front-title">VELMAR INDUSTRIAL COATINGS INC.</h1>
    <div class="front-web">www.Velmarfloors.com</div>
  </section>

  <section class="card card-back">
    <div class="brand">
      <span class="brand-square"></span>
      <span class="brand-name">VELMAR INDUSTRIAL COATINGS INC.</span>
    </div>

    <div class="person">
      <div class="person-name">ROB HALE</div>
      <div class="person-tollfree">1-800-555-0142</div>
    </div>

    <address class="address">
      Velmar Inc.<br>
      PO Box 42<br>
      Riverton, WA 98500
    </address>

    <ul class="contacts">
      <li>(360) 555-0131
        <svg viewBox="0 0 24 24" aria-hidden="true"><path d="M6.6 10.8a15 15 0 0 0 6.6 6.6l2.2-2.2c.3-.3.7-.4 1-.2 1.1.4 2.3.6 3.6.6.6 0 1 .4 1 1V20c0 .6-.4 1-1 1A17 17 0 0 1 3 4c0-.6.4-1 1-1h3.5c.6 0 1 .4 1 1 0 1.3.2 2.5.6 3.6.1.3 0 .7-.2 1z"/></svg>
      </li>
      <li>(360) 555-0133
        <svg viewBox="0 0 24 24" aria-hidden="true"><path d="M7 2h10a2 2 0 0 1 2 2v16a2 2 0 0 1-2 2H7a2 2 0 0 1-2-2V4a2 2 0 0 1 2-2zm0 2v16h10V4z"/></svg>
      </li>
      <li>(360) 555-0177
        <svg viewBox="0 0 24 24" aria-hidden="true"><path d="M6 2h9l3 3v4h2a2 2 0 0 1 2 2v9a2 2 0 0 1-2 2H4a2 2 0 0 1-2-2v-9a2 2 0 0 1 2-2h2zm2 2v5h8V6h-2V4zm2 9v2h2v-2zm4 0v2h2v-2zm-4 3v2h2v-2zm4 0v2h2v-2z"/></svg>
      </li>
      <li>rob@velmarfloors.com
        <svg viewBox="0 0 24 24" aria-hidden="true"><path d="M2 5h20v14H2zm2 2v.5l8 5 8-5V7zm0 3v7h16v-7l-8 5z"/></svg>
      </li>
    </ul>
  </section>
</main>
</body>
</html>
```